Business Card Design Project - Tall Maple

We are looking for a new business card design. Our company name is Tall Maple Communication Solutions. Our primary function is to provide our clients with communication solutions. These solutions include commercial phone systems and T1 and Fiber Internet lines. Another major part of the business is cabling new buildings with CAT5 cable for both data and phone.

Industry/Entity Type

Communication

Requirements
Must have
• The cards need to be two sided and have some bleeding edge color.
Nice to have
• We are going to upload our current logo BUT we are not married to this logo. If you want to incorporate a re-designed logo with the new business card - please feel free to do so. We are looking for a new bold look that is very colorful yet professional.

```html
<!DOCTYPE html>
<html lang="en">
<head>
<meta charset="utf-8">
<title>Tall Maple Communication Solutions – Business Card</title>
<link rel="stylesheet" href="https://fonts.googleapis.com/css2?family=Figtree:wght@400;600&family=Oswald:wght@400&display=swap">
<style>
  :root {
    --backdrop: #f3f3f1;
    --navy: #022c5f;
    --white: #ffffff;
  }
  * { margin: 0; padding: 0; box-sizing: border-box; }
  html, body {
    width: 1200px;
    height: 900px;
    overflow: hidden;
    background: var(--backdrop);
  }
  .canvas {
    position: relative;
    width: 1200px;
    height: 900px;
  }
  .card {
    position: absolute;
    left: 319px;
    width: 590px;
    height: 382px;
    background: var(--navy);
    color: var(--white);
    font-family: "Figtree", "Helvetica Neue", Arial, sans-serif;
  }
  .card--front { top: 48px; }
  .card--back { top: 475px; }

  /* Front side */
  .brand-small {
    position: absolute;
    top: 108px;
    right: 30px;
    display: flex;
    align-items: center;
    gap: 10px;
    font-weight: 600;
    font-size: 22px;
    line-height: 1;
  }
  .brand-dot {
    display: block;
    flex: none;
    border-radius: 50%;
    background: var(--white);
  }
  .brand-small .brand-dot { width: 18px; height: 18px; }

  .contact {
    position: absolute;
    left: 30px;
    top: 143px;
    font-size: 15px;
    line-height: 20.5px;
  }
  .contact__name {
    font-weight: 600;
    font-size: 16.5px;
    margin-bottom: 10px;
  }
  .contact__group + .contact__group { margin-top: 10px; }

  /* Back side */
  .brand-large {
    position: absolute;
    left: 0;
    right: 0;
    top: 135px;
    display: flex;
    justify-content: center;
    align-items: center;
    gap: 18px;
    font-weight: 600;
    font-size: 54px;
    line-height: 1;
  }
  .brand-large .brand-dot { width: 40px; height: 40px; }

  .tagline {
    position: absolute;
    left: 0;
    right: 0;
    top: 276px;
    text-align: center;
    font-family: "Oswald", "Arial Narrow", sans-serif;
    font-weight: 400;
    font-size: 24px;
    line-height: 31px;
    letter-spacing: 5.5px;
    text-transform: uppercase;
  }
</style>
</head>
<body>
<main class="canvas">
  <section class="card card--front" aria-label="Business card, contact side">
    <div class="brand-small">
      <span class="brand-dot" aria-hidden="true"></span>
      <span class="brand-name">Tall Maple</span>
    </div>
    <div class="contact">
      <p class="contact__name">Nora Whitfield</p>
      <div class="contact__group">
        <p>Office: 602 555 0148</p>
        <p>Cell: 602 555 0172</p>
        <p>24/7: 800 555 0190</p>
        <p>Fax: 800 555 0136</p>
      </div>
      <div class="contact__group">
        <p>1840 N Saguaro Avenue, Suite 410</p>
        <p>Mesa, AZ 85201</p>
      </div>
      <div class="contact__group">
        <p>www.tallmaplecomms.com</p>
        <p>support@tallmaplecomms.com</p>
      </div>
    </div>
  </section>

  <section class="card card--back" aria-label="Business card, brand side">
    <div class="brand-large">
      <span class="brand-dot" aria-hidden="true"></span>
      <span class="brand-name">Tall Maple</span>
    </div>
    <p class="tagline">Communication<br>Solutions</p>
  </section>
</main>
</body>
</html>
```